My name is Tomas Berenji, and I have done business with your company several times. I need a business card to represent my business, I own a company by the name of VELMINO Suntan Lotion & Sunscreen.
My requirements are as follow: My company logo in the brightest gold possible, on a black, grainy (sandy) background, with shading around the each element. With the company name in gold, a stylized coconut trees, and some type of wave graphic in gold. "A product of the USA, Staten Island, NY"
"For comments, suggestion, or ordering please contact us at:
velmino42@brisalto.com"

"VELMINO™ Tanning Lotion & Sunscreen―Crafted with Care"

Velmino Tanning Lotion & Sunscreen is the most extraordinary and innovative sun tanning product to emerge in several generations. The constituents of this product are formidable substances that protect the skin against the aftermath of sun exposure−before you exposed yourself to the sun’s rays. The Aloe Vera in this product, along with other oils and cream, are specifically manufactured to lessen the symptoms of extended exposure to the sun. Velmino is designed to provide a Broad Spectrum Protection (50) that assist in the reduction of (UVA) and (UVB) radiation to create a magnificent sun-absorbing, long-lasting, deep dark bronzing experience.
Thank you,
Tomas Berenji
tomasbberenji@nexipost.com

Target Market(s)

Sunscreen

Industry/Entity Type

Business

Contact Information for Business Card

VELMINO™ Tanning Lotion and Sunscreen
Crafted with Care

Velmino Tanning Lotion is the most extraordinary and innovative sun tanning product to emerge in several generations. The constituents of this product are formidable substances that protect the skin against the aftermath of sun exposure−before you exposed yourself to the sun’s rays. The Aloe Vera, in this product, along with other oils and cream, are specifically manufactured to lessen the symptoms of extended exposure to the sun. Velmino protects your skin from dehydration and treat your skin with the products we apply to ourselves after a sunburn−before the sun tanning process begins. Velmino is designed to provide a Broad Spectrum Protection (50) that assist in the reduction of (UVA) and (UVB) radiation to create a magnificent sun-absorbing, long-lasting, deep dark bronzing experience.

Colors
fece3e
acd136

Requirements
Must have
• Black Card Stock with grainy surface, Gold Logo, stylized Coconut Palm Tree, Company Name, email address, and NYC location.
• Modern Layout with Modern fonts and graphics

```html
<!DOCTYPE html>
<html lang="en">
<head>
<meta charset="utf-8">
<title>Velmino Suntan Lotion – Business Card</title>
<link href="https://fonts.googleapis.com/css2?family=Cinzel:wght@700&family=Montserrat:wght@400;500;600;700&display=swap" rel="stylesheet">
<style>
  :root {
    --stage: #2b2b2b;
    --card-black: #050505;
    --card-white: #ffffff;
    --gold: #d9a62a;
    --gold-light: #fece3e;
    --green: #2f9a34;
    --text-dark: #333333;
    --white: #ffffff;
  }
  * { box-sizing: border-box; margin: 0; padding: 0; }
  html, body { width: 1200px; height: 900px; overflow: hidden; }
  body { background: var(--stage); position: relative; font-family: "Montserrat", sans-serif; }

  .card {
    position: absolute;
    width: 620px;
    height: 354px;
    border-radius: 22px;
    overflow: hidden;
    box-shadow: 0 14px 30px rgba(0,0,0,.55);
  }

  /* Front */
  .card--front { left: 60px; top: 70px; background: var(--card-black); }
  .brand-mark {
    position: absolute; left: 50%; top: 46px; transform: translateX(-50%);
    width: 104px; height: 104px; border-radius: 50%;
    background: var(--gold);
  }
  .brand-name {
    position: absolute; left: 0; right: 0; top: 160px; text-align: center;
    font-family: "Cinzel", serif; font-weight: 700; color: var(--white);
    font-size: 58px; letter-spacing: 2px; line-height: 1;
  }
  .brand-tagline {
    position: absolute; left: 0; right: 0; top: 226px; text-align: center;
    font-family: "Cinzel", serif; font-weight: 700; color: var(--white);
    font-size: 24px; letter-spacing: 1px; line-height: 1.2;
  }
  .front-web {
    position: absolute; left: 0; right: 0; top: 288px; text-align: center;
    font-size: 16px; font-weight: 500; color: var(--white); white-space: nowrap;
  }
  .front-web .domain { color: var(--gold-light); font-weight: 600; }

  /* Back */
  .card--back { left: 520px; top: 476px; background: var(--card-white); }
  .back-emblem { position: absolute; right: 0; top: 0; width: 300px; height: 354px; }
  .back-brand {
    position: absolute; right: 52px; top: 92px; width: 200px; text-align: center;
  }
  .back-brand .brand-dot {
    width: 120px; height: 120px; border-radius: 50%; background: var(--gold);
    margin: 0 auto 14px;
  }
  .back-brand .brand-word {
    font-family: "Cinzel", serif; font-weight: 700; color: var(--gold-light);
    font-size: 26px; letter-spacing: 2px;
  }

  .contact { position: absolute; left: 44px; top: 148px; color: var(--text-dark); }
  .contact__name { font-size: 25px; font-weight: 700; color: var(--green); line-height: 1.1; }
  .contact__role { font-size: 14px; margin: 3px 0 14px; }
  .contact__address { font-size: 15px; line-height: 1.35; margin: 0 0 10px; }
  .contact__list { list-style: none; font-size: 15px; line-height: 1.4; }
  .contact__item { display: flex; align-items: center; gap: 10px; white-space: nowrap; }
  .contact__icon { width: 13px; height: 13px; fill: var(--green); flex: none; }
  .contact__web .domain { color: var(--green); font-weight: 700; }
</style>
</head>
<body>

  <section class="card card--front">
    <div class="brand-mark"></div>
    <div class="brand-name">VELMINO</div>
    <div class="brand-tagline">SUNTAN LOTION</div>
    <div class="front-web">www.<span class="domain">velminosuntanlotion</span>.com</div>
  </section>

  <section class="card card--back">
    <svg class="back-emblem" viewBox="0 0 300 354" aria-hidden="true">
      <circle cx="215" cy="150" r="214" fill="none" stroke="#2f9a34" stroke-width="3"/>
      <circle cx="222" cy="150" r="206" fill="#050505"/>
    </svg>
    <div class="back-brand">
      <div class="brand-dot"></div>
      <div class="brand-word">VELMINO</div>
    </div>

    <div class="contact">
      <div class="contact__name">Marek Solvane</div>
      <div class="contact__role">Director</div>
      <div class="contact__address">48 Harbor Lane<br>Port Edan, NY 10987</div>
      <ul class="contact__list">
        <li class="contact__item"><svg class="contact__icon" viewBox="0 0 24 24"><path d="M6.6 10.8a15 15 0 0 0 6.6 6.6l2.2-2.2a1 1 0 0 1 1-.25 11.4 11.4 0 0 0 3.6.57 1 1 0 0 1 1 1V20a1 1 0 0 1-1 1A17 17 0 0 1 3 4a1 1 0 0 1 1-1h3.5a1 1 0 0 1 1 1c0 1.25.2 2.45.57 3.57a1 1 0 0 1-.25 1z"/></svg><span>+330 5817-2294</span></li>
        <li class="contact__item"><svg class="contact__icon" viewBox="0 0 24 24"><path d="M2 5h20v14H2zm2 2v.5l8 5 8-5V7zm0 2.8V17h16V9.8l-8 5z"/></svg><span>velmino42@brisalto.com</span></li>
        <li class="contact__item"><svg class="contact__icon" viewBox="0 0 24 24"><path d="M12 2a10 10 0 1 0 0 20 10 10 0 0 0 0-20zm6.9 6h-3a15 15 0 0 0-1.3-3.9A8 8 0 0 1 18.9 8zM12 4c.9 1.2 1.6 2.5 2 4h-4c.4-1.5 1.1-2.8 2-4zM4.3 14a8 8 0 0 1 0-4h3.4a16 16 0 0 0 0 4zm.8 2h3a15 15 0 0 0 1.3 3.9A8 8 0 0 1 5.1 16zm3-8h-3a8 8 0 0 1 4.3-3.9A15 15 0 0 0 8.1 8zM12 20c-.9-1.2-1.6-2.5-2-4h4c-.4 1.5-1.1 2.8-2 4zm2.3-6H9.7a14 14 0 0 1 0-4h4.6a14 14 0 0 1 0 4zm.3 5.9A15 15 0 0 0 15.9 16h3a8 8 0 0 1-4.3 3.9zm1.7-5.9a16 16 0 0 0 0-4h3.4a8 8 0 0 1 0 4z"/></svg><span class="contact__web">www.<span class="domain">velminosuntanlotion</span>.com</span></li>
      </ul>
    </div>
  </section>

</body>
</html>
```